Referral Card thats different from the rest

Business card size-

Referral card that will be given to clients, in turn they will pass it on to their friends.

The referee will add their name and address, and friends name to card before it is passed on

Referee gets 2 FREE movie tickets

Friend gets $25 OFF their service

Company is an electrical contracting company specialising in the domestic market.

I would like the card to be fun not so serious!
Completely open minded to any and every creative idea!

attached is 2 photo of an example of what another business has, i am trying to achieve something similiar
Updates

I have increased the budget, ;)

i have added 2 x photos of what i am trying to achieve. this is from another business, I am after something similar to this
Thanks

I have updated the design brief.
this should help make it easir and more clear
Thanks

Target Market(s)

Home owners from 30yrs +

Industry/Entity Type

Electrical

Requirements
Must have
• Logo - Not a main feature of card
1300 574 862 on both sides
Lic no: 381946D (doesn’t have to be big) prefer on back

The main feature of the front of the card is the 2 free movie tickets for Referee & $25 OFF Friends first bill

HOW ABOUT TWO FREE MOVIE TICKETS?
It is easy! Know someone who needs an electrician? Maybe a friend, family member, relative or work colleague.
Tell them about us, and we will take $25 off their first bill and give you two FREE Movie Tickets just for introducing us.
To make a referral fill out this card and give it to your friend.

Recommended By:____________
Address:__________________
Frinds name: _____________

*this offer is only valued for work over $55. Non transferable for cash. This coupon is limited to 1 per customer, not to be used in conjunction with any other offer
Nice to have
• Catchy heading on card
example- tell a friend for cash card, (if i was giving away cash vouchers..)

example- keep me in your wallet and pass me on

```html
<!DOCTYPE html>
<html lang="en">
<head>
<meta charset="utf-8">
<title>Referral Card – Front and Back</title>
<link rel="stylesheet" href="https://fonts.googleapis.com/css2?family=Anton&family=Arimo:wght@400;700&display=swap">
<style>
  :root {
    --stage: #d9dadc;
    --blue-deep: #1463b8;
    --blue-mid: #2a86d6;
    --blue-light: #56b4ee;
    --band-blue: #1aa0dc;
    --heading-blue: #1796d6;
    --yellow: #f7ea1c;
    --red: #e2231a;
    --orange: #f7941d;
    --white: #ffffff;
    --ink: #231f20;
  }
  * { box-sizing: border-box; margin: 0; padding: 0; }
  html, body {
    width: 1200px; height: 457px; overflow: hidden;
    background: var(--stage);
    font-family: "Arimo", Arial, sans-serif;
  }
  .card {
    position: absolute; top: 85px;
    width: 514px; height: 286px; overflow: hidden;
  }

  /* ---------- Front ---------- */
  .card-front {
    left: 72px;
    background:
      linear-gradient(115deg, transparent 38%, rgba(255,255,255,.14) 38%, rgba(255,255,255,.14) 52%, transparent 52%),
      linear-gradient(150deg, transparent 55%, rgba(255,255,255,.12) 55%, rgba(255,255,255,.12) 70%, transparent 70%),
      linear-gradient(160deg, var(--blue-deep) 0%, var(--blue-mid) 55%, var(--blue-light) 100%);
    color: var(--white);
  }
  .front-tagline {
    position: absolute; left: 20px; top: 12px;
    font-weight: 700; font-size: 22.5px; color: var(--yellow);
    letter-spacing: -.3px;
  }
  .front-offer-main {
    position: absolute; left: 18px; top: 44px;
    font-family: "Anton", Impact, sans-serif; font-size: 50px; line-height: 1;
    color: var(--red);
    -webkit-text-stroke: 5px var(--white); paint-order: stroke fill;
    letter-spacing: -.5px;
  }
  .front-offer-sub {
    position: absolute; left: 20px; top: 99px;
    font-family: "Anton", Impact, sans-serif; font-size: 22px; line-height: 1;
    color: var(--red);
    -webkit-text-stroke: 4px var(--white); paint-order: stroke fill;
  }
  .front-discount {
    position: absolute; left: 18px; top: 133px;
    font-family: "Anton", Impact, sans-serif; font-size: 30px; line-height: 1;
    color: var(--orange);
    -webkit-text-stroke: 4px var(--white); paint-order: stroke fill;
  }
  .front-phone {
    position: absolute; left: 20px; top: 198px;
    font-weight: 700; font-size: 37px; letter-spacing: .5px;
  }
  .front-web {
    position: absolute; left: 20px; top: 251px;
    font-size: 12.5px;
  }
  .front-logo-disc {
    position: absolute; right: -48px; bottom: -70px;
    width: 230px; height: 230px; border-radius: 50%;
    background: var(--white);
  }
  .front-mascot {
    position: absolute; right: 14px; top: 112px;
    width: 118px; height: 120px; border-radius: 10px;
    background: linear-gradient(160deg, #f6d2a8, #f39a3a 55%, #3a9a45);
  }
  .front-brand {
    position: absolute; right: 12px; top: 236px; width: 130px;
    font-weight: 700; font-size: 13px; line-height: 1.1; text-align: center;
    color: var(--orange);
  }

  /* ---------- Back ---------- */
  .card-back { left: 613px; background: var(--white); color: var(--ink); }
  .back-heading {
    position: absolute; left: 0; right: 0; top: 24px; text-align: center;
    font-weight: 700; font-size: 22px; color: var(--heading-blue);
  }
  .back-intro {
    position: absolute; left: 24px; right: 24px; top: 53px; text-align: center;
    font-size: 8.4px; line-height: 1.3;
  }
  .back-band {
    position: absolute; left: 0; right: 0; top: 97px; height: 41px;
    background: var(--band-blue);
  }
  .back-phone {
    position: absolute; left: 92px; top: 100px;
    font-weight: 700; font-size: 36px; letter-spacing: .5px; color: var(--white);
  }
  .back-hand {
    position: absolute; left: 0; top: 72px;
    width: 68px; height: 214px; border-radius: 0 30px 0 0;
    background: linear-gradient(180deg, #cfe6f7, #f3c8a0 45%, #e2573a 80%, #3a9a45);
  }
  .referral-form { position: absolute; left: 90px; top: 160px; width: 350px; list-style: none; }
  .form-field { display: flex; align-items: flex-end; height: 21.5px; font-size: 15px; }
  .form-field .line { flex: 1; border-bottom: 1px solid var(--ink); margin-left: 6px; margin-bottom: 3px; }
  .back-terms {
    position: absolute; left: 90px; top: 236px; width: 270px;
    font-size: 8.4px; line-height: 1.3;
  }
  .back-licence {
    position: absolute; right: 20px; top: 263px;
    font-size: 9.5px; color: var(--heading-blue);
  }
</style>
</head>
<body>
  <section class="card card-front" aria-label="Referral card front">
    <p class="front-tagline">Keep Me In Your Wallet And Pass Me On</p>
    <p class="front-offer-main">2 free movie tickets</p>
    <p class="front-offer-sub">for Refcree</p>
    <p class="front-discount">$25 OFF Friends first bill</p>
    <p class="front-phone">1300 574 862</p>
    <p class="front-web">www.brightsparkelectrical.com.au</p>
    <div class="front-logo-disc"></div>
    <div class="front-mascot" role="img" aria-label="Cartoon superhero electrician holding a light bulb"></div>
    <p class="front-brand">Bright Spark Electrical Pty Ltd</p>
  </section>

  <section class="card card-back" aria-label="Referral card back">
    <h1 class="back-heading">HOW ABOUT TWO FREE MOVIE TICKETS?</h1>
    <p class="back-intro">It is easy! Know someone who needs an electrician? Maybe a friend, family member, relative or work colleague. Tell them about us, and we will take $25 off their first bill and give you two FREE Movie Tickets just for introducing us. To make a referral fill out this card and give it to your friend.</p>
    <div class="back-band"></div>
    <p class="back-phone">1300 574 862</p>
    <div class="back-hand" role="img" aria-label="Illustrated hand holding up a light bulb"></div>
    <ul class="referral-form">
      <li class="form-field">Recommended By:<span class="line"></span></li>
      <li class="form-field">Address:<span class="line"></span></li>
      <li class="form-field">Frinds name:<span class="line"></span></li>
    </ul>
    <p class="back-terms">*this offer is only valued for work over $55. Non transferable for cash. This coupon is limited to 1 per customer, not to be used in conjunction with any other offer.</p>
    <p class="back-licence">Lic no: 381946D</p>
  </section>
</body>
</html>
```